TBNW site redesign

Please redesign a home page with content provided. PSD only - no coding
Can use any images from Vexelmarq.com

Please create a site design that more clearly illustrates the client's services and expertise. We are looking for a high-end design.

Any images used must be generic or of Dallas TX.

Fonts: Any
Colors: Match to logo
Look: Modern - Professional

Target Market(s)

medium-large business owners

Number of Pages Required

1 page

Font styles to use
Serif
Sans Serif

Requirements
Must have
• cohesive professional design
• high end look
• Match to logo

```html
<!DOCTYPE html>
<html lang="en">
<head>
<meta charset="utf-8">
<title>TBNW – Professional Office and Warehouse Leasing</title>
<link rel="stylesheet" href="https://fonts.googleapis.com/css2?family=Montserrat:wght@300;400;500;600;700;800&family=Playfair+Display:wght@400&display=swap">
<style>
  :root {
    --brand-red: #e8303a;
    --ink: #1d1f24;
    --muted: #6c7078;
    --faint: #ececee;
    --white: #ffffff;
    --sky-top: #4f86b0;
    --sky-mid: #7aa6c6;
    --glass: #1f6e8f;
  }
  * { box-sizing: border-box; margin: 0; padding: 0; }
  html, body { width: 1200px; height: 892px; overflow: hidden; background: var(--white); }
  body { font-family: "Montserrat", sans-serif; color: var(--ink); position: relative; }

  .site-header {
    position: absolute; top: 0; left: 0; width: 1200px; height: 63px;
    background: var(--white); display: flex; align-items: center;
  }
  .brand { position: absolute; left: 150px; top: 18px; display: flex; align-items: center; gap: 8px; }
  .brand-mark { width: 16px; height: 16px; background: var(--brand-red); }
  .brand-name { font-weight: 700; font-size: 20px; letter-spacing: 2px; color: var(--ink); }

  .main-nav { position: absolute; top: 0; left: 0; height: 63px; width: 1200px; }
  .main-nav a {
    position: absolute; top: 0; height: 63px; line-height: 63px;
    font-size: 13px; font-weight: 500; color: var(--ink); text-decoration: none;
    transform: translateX(-50%); white-space: nowrap;
  }
  .main-nav a.is-active::after {
    content: ""; position: absolute; left: -8px; right: -8px; bottom: 0; height: 3px; background: var(--brand-red);
  }

  .hero {
    position: absolute; top: 63px; left: 0; width: 1200px; height: 520px; overflow: hidden;
  }
  .hero-photo {
    position: absolute; inset: 0;
    background:
      linear-gradient(115deg, var(--sky-top) 0%, var(--sky-mid) 45%, rgba(255,255,255,0) 46%),
      linear-gradient(160deg, #3d8aa8 0%, var(--glass) 60%, #174f69 100%);
  }
  .hero-copy { position: absolute; left: 151px; top: 148px; color: var(--white); }
  .hero-title { font-size: 38px; line-height: 1.2; letter-spacing: 0.5px; }
  .hero-title .light { display: block; font-weight: 300; }
  .hero-title .bold { display: block; font-weight: 800; font-size: 40px; }
  .hero-lede { margin-top: 20px; width: 570px; font-size: 14px; line-height: 23px; font-weight: 500; }
  .btn {
    display: inline-block; background: var(--brand-red); color: var(--white);
    font-weight: 700; font-size: 12px; letter-spacing: 0.8px; text-decoration: none;
  }
  .hero-cta { margin-top: 24px; padding: 13px 16px; }

  .why-section { position: absolute; top: 583px; left: 0; width: 1200px; height: 309px; text-align: center; }
  .why-backdrop {
    position: absolute; top: 50px; left: 0; width: 1200px;
    font-family: "Playfair Display", serif; font-size: 40px; letter-spacing: 14px; color: var(--faint);
  }
  .why-title {
    position: absolute; top: 78px; left: 0; width: 1200px;
    font-size: 15px; font-weight: 700; letter-spacing: 4px; color: var(--ink);
  }
  .why-rule { position: absolute; top: 104px; left: 578px; width: 44px; height: 2px; background: var(--brand-red); }

  .benefits { position: absolute; top: 132px; left: 240px; width: 720px; display: flex; justify-content: space-between; }
  .benefit { width: 210px; }
  .benefit-icon { width: 30px; height: 30px; display: block; margin: 0 auto; }
  .benefit-title { margin-top: 10px; font-size: 10px; font-weight: 700; letter-spacing: 1px; }
  .benefit-text { margin-top: 8px; font-size: 10px; line-height: 15px; color: var(--muted); }
  .why-cta { position: absolute; top: 262px; left: 551px; padding: 8px 14px; font-size: 10px; }
</style>
</head>
<body>
  <header class="site-header">
    <div class="brand">
      <span class="brand-mark"></span>
      <span class="brand-name">TBNW</span>
    </div>
    <nav class="main-nav">
      <a class="is-active" href="#" style="left:457px">HOME</a>
      <a href="#" style="left:546px">SERVICES</a>
      <a href="#" style="left:658px">ABOUT TBNW</a>
      <a href="#" style="left:790px">CONTACT US</a>
      <a href="#" style="left:887px">BLOG</a>
      <a href="#" style="left:980px">MARKET NEWS</a>
    </nav>
  </header>

  <section class="hero">
    <div class="hero-photo" role="img" aria-label="Glass office tower seen from below against a blue sky"></div>
    <div class="hero-copy">
      <h1 class="hero-title">
        <span class="light">PROFESSIONAL OFFICE</span>
        <span class="bold">AND WAREHOUSE LEASING</span>
      </h1>
      <p class="hero-lede">Fast-track your search with tenant reps that only serve you, and specialize in the DFW area.</p>
      <a class="btn hero-cta" href="#">CONTACT US NOW</a>
    </div>
  </section>

  <section class="why-section">
    <div class="why-backdrop" aria-hidden="true">REPRESENTATION</div>
    <h2 class="why-title">WHY TENANT REPRESENTATION</h2>
    <span class="why-rule"></span>
    <div class="benefits">
      <div class="benefit">
        <svg class="benefit-icon" viewBox="0 0 30 30" fill="none" stroke="#e8303a" stroke-width="2">
          <path d="M15 25 L5 15 A5 5 0 0 1 15 8 A5 5 0 0 1 25 15 Z"/>
        </svg>
        <h3 class="benefit-title">RELATIONSHIPS</h3>
        <p class="benefit-text">Save time by trusting reps who know every building and negotiate the right space for your team.</p>
      </div>
      <div class="benefit">
        <svg class="benefit-icon" viewBox="0 0 30 30" fill="none" stroke="#e8303a" stroke-width="2">
          <circle cx="20" cy="10" r="5"/><path d="M16 14 L6 24 M9 21 L12 24 M11 19 L13 21"/>
        </svg>
        <h3 class="benefit-title">ACCESS TO MORE</h3>
        <p class="benefit-text">We have direct access to listings and owners, so you see options before they reach the open market.</p>
      </div>
      <div class="benefit">
        <svg class="benefit-icon" viewBox="0 0 30 30" fill="none" stroke="#e8303a" stroke-width="2">
          <path d="M5 12 L10 6 H20 L25 12 L15 25 Z M5 12 H25 M12 6 L15 25 L18 6"/>
        </svg>
        <h3 class="benefit-title">FREE TO YOU</h3>
        <p class="benefit-text">You pay us nothing. Our fee comes from the landlord, so our only loyalty is to you.</p>
      </div>
    </div>
    <a class="btn why-cta" href="#">KNOW MORE</a>
  </section>
</body>
</html>
```